Design a Website for an IT Support Company

We are an IT support company that provides commercial IT support and services to small and medium sized businesses. We are in need of a website to be developed for our business.
We would like to work with someone who is either familiar with the IT field, or has developed a website for an IT support company in the past.
Some examples of designs/layouts that we like:
https://www.veltragrid.example/
http://www.morvashelp.example/
http://kelbo.example/
http://www.nuvopathsystems.example/
http://www.quordesk.example/
I have attached a word document that gives a menu system/page layout format that we would like for our website as well as branch office phone numbers. Our logo is also attached that you can use for your design purposes. We currently do not have copy produced for all of the pages outlined in the word document, but would get this done during the project with the selected designer.
We would like the website to be SEO friendly & fully responsive. We would prefer a Wordpress format, however, we are open to HTML formats as well.

```html
<!DOCTYPE html>
<html lang="en">
<head>
<meta charset="utf-8">
<title>Brisklane IT – IT Support & Wireless Internet Service Provider</title>
<link rel="stylesheet" href="https://fonts.googleapis.com/css2?family=Montserrat:wght@400;500;600;700&family=Open+Sans:ital,wght@0,400;0,600;0,700;1,400&display=swap">
<style>
:root{
  --navy:#1d2b44;
  --blue:#0f6fb8;
  --blue-band:#0d55a0;
  --footer:#1a5d9f;
  --footer-dark:#164c84;
  --ink:#222;
  --text:#444;
  --muted:#8a8a8a;
  --gray-btn:#7b7b7b;
  --green:#5db646;
  --light:#f7f7f7;
  --line:#e2e2e2;
}
*{margin:0;padding:0;box-sizing:border-box}
html,body{width:1200px;height:2628px;overflow:hidden;background:#fff}
body{position:relative;font-family:"Open Sans",Arial,sans-serif;color:var(--text)}
a{color:inherit;text-decoration:none}
ul{list-style:none}

/* header */
.site-header{position:absolute;left:0;top:0;width:1200px;height:121px;background:#fff}
.brand{position:absolute;display:flex;align-items:center;gap:10px;font-family:"Montserrat",sans-serif;font-weight:600;color:var(--navy);white-space:nowrap}
.brand-dot{border-radius:50%;background:var(--blue);flex:none}
.site-header .brand{left:88px;top:30px;font-size:32px}
.site-header .brand-dot{width:40px;height:40px}
.header-contact{position:absolute;top:30px;font-size:15px;color:#333;display:flex;align-items:center;gap:8px;white-space:nowrap}
.main-nav{position:absolute;top:74px;left:0;font-family:"Montserrat",sans-serif;font-size:16px;font-weight:600;color:#222}
.main-nav a{position:absolute;white-space:nowrap}
.main-nav .active{color:var(--blue)}

/* hero */
.hero{position:absolute;left:0;top:121px;width:1200px;height:559px;background:linear-gradient(90deg,#f1f1f1 0%,#e8e8e8 40%,#c9cdd3 60%,#7c828c 85%,#3c4350 100%)}
.hero-kicker{position:absolute;left:82px;top:164px;font-size:25px;color:#333;font-weight:400;white-space:nowrap}
.hero-title{position:absolute;left:82px;top:198px;font-size:30px;color:#111;font-weight:600;white-space:nowrap}
.btn{position:absolute;display:flex;align-items:center;justify-content:center;color:#fff;font-family:"Montserrat",sans-serif;font-weight:600;white-space:nowrap}
.btn-consult{left:86px;top:273px;width:212px;height:56px;background:var(--gray-btn);font-size:16px}
.btn-support{left:317px;top:273px;width:210px;height:56px;background:var(--blue);font-size:17px}

/* welcome */
.welcome-title{position:absolute;left:0;width:1200px;top:730px;text-align:center;font-family:"Montserrat",sans-serif;font-weight:500;font-size:37px;color:#222}
.welcome-sub{position:absolute;left:0;width:1200px;top:793px;text-align:center;font-size:20px;color:#1a55a5}
.service{position:absolute;top:890px;width:340px;text-align:center}
.service-icon{width:108px;height:108px;border-radius:50%;background:var(--green);margin:0 auto}
.service h3{font-family:"Montserrat",sans-serif;font-weight:500;font-size:21px;color:var(--blue);margin-top:26px}
.service ul{margin-top:8px;font-size:13.5px;line-height:20.7px;color:#333}

/* why band */
.why-band{position:absolute;left:0;top:1354px;width:1200px;height:319px;background:var(--blue-band)}
.why-title{position:absolute;left:98px;top:1390px;font-family:"Montserrat",sans-serif;font-weight:500;font-size:29px;color:#fff}
.why-copy{position:absolute;left:98px;top:1441px;width:420px;font-size:13.5px;line-height:20px;color:#fff}
.why-copy p+p{margin-top:20px}
.btn-more{position:absolute;left:98px;top:1582px;width:119px;height:35px;background:#fff;color:var(--blue-band);font-size:12.5px;font-weight:700;display:flex;align-items:center;justify-content:center;border-radius:2px}
.slider-dots{position:absolute;left:441px;top:1636px;display:flex;gap:7px}
.slider-dots span{width:9px;height:9px;background:#9bb5d4}
.slider-dots .on{background:#fff}
.why-rings{position:absolute;left:560px;top:1290px}
.why-photo{position:absolute;left:610px;top:1300px;width:470px;height:420px;border-radius:50%;background:radial-gradient(circle,#dfe6ec 0%,#a9b3bd 45%,#6f6f73 70%,rgba(80,80,85,0) 72%)}

/* testimonials & news */
.testimonial-card{position:absolute;left:26px;top:1761px;width:640px;height:394px;background:var(--light)}
.testimonial-title{position:absolute;left:26px;width:640px;top:1800px;text-align:center;font-family:"Montserrat",sans-serif;font-weight:500;font-size:28px;color:#222}
.quote-nav{position:absolute;left:26px;width:640px;top:1870px;display:flex;justify-content:center;align-items:center;gap:26px}
.quote-text{position:absolute;left:76px;width:540px;top:1930px;text-align:center;font-style:italic;font-size:15px;line-height:31px;color:#8a8a8a}
.quote-name{position:absolute;left:26px;width:640px;top:2044px;text-align:center;font-style:italic;font-size:14px;color:#666}
.quote-role{position:absolute;left:26px;width:640px;top:2075px;text-align:center;font-size:11px;color:#444}
.news-divider{position:absolute;left:718px;top:1796px;width:1px;height:324px;background:var(--line)}
.news-panel{position:absolute;left:745px;top:1761px;width:396px;height:394px;background:var(--light)}
.news-title{position:absolute;left:776px;top:1790px;font-family:"Montserrat",sans-serif;font-weight:500;font-size:22px;color:#222}
.news-all{position:absolute;left:777px;top:1823px;font-size:9.5px;font-style:italic;color:#444}
.news-item{position:absolute;left:778px;width:300px;height:86px;border-bottom:1px solid var(--line)}
.news-thumb{position:absolute;left:0;top:0;width:61px;height:61px;background:linear-gradient(135deg,#8e7a66,#3f3a35)}
.news-item h4{position:absolute;left:77px;top:2px;font-weight:400;font-size:14px;color:#333;white-space:nowrap}
.news-meta{position:absolute;left:77px;top:30px;font-size:10px;color:#555;display:flex;gap:20px;white-space:nowrap}

/* cta */
.cta-blue{position:absolute;left:0;top:2234px;width:1200px;height:94px;background:var(--blue-band)}
.cta-call{position:absolute;left:0;top:2216px}
.cta-small{position:absolute;left:0;width:499px;top:2236px;text-align:right;font-family:"Montserrat",sans-serif;font-size:19px;color:#333}
.cta-phone{position:absolute;left:0;width:496px;top:2268px;text-align:right;font-family:"Montserrat",sans-serif;font-weight:600;font-size:33px;color:#fff}
.quote-title{position:absolute;left:583px;top:2248px;font-family:"Montserrat",sans-serif;font-weight:600;font-size:21px;color:#fff}
.field{position:absolute;top:2290px;height:33px;background:#dbe3ec;color:#888;font-size:13px;padding:8px 10px}
.btn-subscribe{position:absolute;left:1004px;top:2290px;width:103px;height:33px;background:#9a9a9a;color:#fff;font-family:"Montserrat",sans-serif;font-weight:600;font-size:15px;display:flex;align-items:center;justify-content:center}

/* footer */
.site-footer{position:absolute;left:0;top:2328px;width:1200px;height:265px;background:var(--footer);color:#fff}
.footer-head{position:absolute;top:62px;font-family:"Montserrat",sans-serif;font-weight:600;font-size:22px;white-space:nowrap}
.footer-links{position:absolute;top:116px;font-size:13px;line-height:22px;white-space:nowrap}
.contact-row{position:absolute;left:415px;display:flex;gap:14px;align-items:flex-start;font-size:12px;white-space:nowrap}
.contact-ico{width:25px;height:25px;border-radius:50%;background:#c7ccd3;flex:none}
.social-row{position:absolute;left:689px;display:flex;align-items:center;gap:14px;font-size:12px}
.social-ico{width:28px;height:28px;border-radius:50%}
.site-footer .brand{left:850px;top:118px;font-size:34px;color:#fff}
.site-footer .brand-dot{width:50px;height:50px;background:#34a8e6}
.copyright{position:absolute;left:0;top:2593px;width:1200px;height:35px;background:var(--footer-dark);color:#fff;font-size:11px;display:flex;align-items:center;justify-content:center}
</style>
</head>
<body>

<header class="site-header">
  <div class="brand"><span class="brand-dot"></span>Brisklane IT</div>
  <div class="header-contact" style="left:760px">
    <svg width="20" height="20" viewBox="0 0 24 24" fill="none" stroke="#555" stroke-width="1.6"><path d="M5 3h4l2 5-2.5 1.5a11 11 0 0 0 6 6L16 13l5 2v4a2 2 0 0 1-2 2A17 17 0 0 1 3 5a2 2 0 0 1 2-2z"/></svg>
    1.800.555.0184
  </div>
  <div class="header-contact" style="left:937px">
    <svg width="22" height="16" viewBox="0 0 22 16" fill="none" stroke="#555" stroke-width="1.5"><rect x="1" y="1" width="20" height="14"/><path d="M1 1l10 8 10-8"/></svg>
    info@brisklane.example
  </div>
  <nav class="main-nav">
    <a class="active" style="left:641px">Home</a>
    <a style="left:735px">Services</a>
    <a style="left:838px">Why Brisklane IT</a>
    <a style="left:1030px">Contact Us</a>
  </nav>
</header>

<section class="hero" role="img" aria-label="Photo of smiling support agents wearing headsets at a help desk">
  <p class="hero-kicker">IT support company that provides commercial IT</p>
  <h1 class="hero-title">Wireless Internet Service Provider</h1>
  <a class="btn btn-consult">Free Consultation Now</a>
  <a class="btn btn-support">Get Support</a>
</section>

<h2 class="welcome-title">Welcome to Brisklane IT</h2>
<p class="welcome-sub">Wireless Internet Service Provider</p>

<div class="service" style="left:75px">
  <div class="service-icon" role="img" aria-label="Icon of a pointing hand and light bulb"></div>
  <h3>Data</h3>
  <ul>
    <li>Managed IT Services</li><li>IT Support &amp; Consulting</li><li>IT Helpdesk Services</li><li>Network Security</li><li>Data Backup &amp; Recovery</li><li>Servers &amp;Virtualization</li><li>Remote Monitoring Services</li><li>Wireless Networking</li><li>Email &amp; Spam Threat Management</li><li>Structured Cabling</li>
  </ul>
</div>
<div class="service" style="left:438px">
  <div class="service-icon" role="img" aria-label="Icon of a clipboard checklist with pen"></div>
  <h3>Cloud</h3>
  <ul>
    <li>Deskora Suite Migrations</li><li>Nimbra Cloud Management Services</li><li>Cloud Migration Services</li><li>Hosted Virtual Servers</li><li>Hosted Telephone Systems</li>
  </ul>
</div>
<div class="service" style="left:787px">
  <div class="service-icon" role="img" aria-label="Icon of a clipboard with a list"></div>
  <h3>Voice</h3>
  <ul>
    <li>Kestrel PBX Consulting</li><li>Business Telephone Systems</li><li>Multiple Office Phone Systems</li><li>Tallwave Telephone Systems</li><li>SIP Trunks</li>
  </ul>
</div>

<section class="why-band"></section>
<svg class="why-rings" width="560" height="460" viewBox="0 0 560 460" fill="none" stroke="#3a78bb" stroke-width="1.2" aria-hidden="true">
  <circle cx="285" cy="230" r="120"/><circle cx="285" cy="230" r="175"/>
</svg>
<div class="why-photo" role="img" aria-label="Overhead photo of business people meeting around a glass table"></div>
<h2 class="why-title">Why Brisklane IT</h2>
<div class="why-copy">
  <p>one of the world's leading financial consulting firms. We work with clients to help Them have a thorough look about their financial situations, make better decisions,</p>
  <p>Ledgerwise is &nbsp;get those decisions translated quickly into actions and sustain the momentum into the future.</p>
</div>
<a class="btn-more">Read More &nbsp;›</a>
<div class="slider-dots"><span></span><span class="on"></span><span></span></div>

<div class="testimonial-card"></div>
<h2 class="testimonial-title">What Clients Say</h2>
<div class="quote-nav">
  <svg width="12" height="18" viewBox="0 0 12 18" fill="none" stroke="#888" stroke-width="2"><path d="M10 2L3 9l7 7"/></svg>
  <svg width="44" height="34" viewBox="0 0 44 34" fill="var(--blue)"><path d="M2 34V20C2 9 8 3 17 1l2 4c-5 2-8 6-8 11h8v18zM25 34V20c0-11 6-17 15-19l2 4c-5 2-8 6-8 11h8v18z"/></svg>
  <svg width="12" height="18" viewBox="0 0 12 18" fill="none" stroke="#888" stroke-width="2"><path d="M2 2l7 7-7 7"/></svg>
</div>
<p class="quote-text">Vestibulum id ligula porta felis euismod semper. Morbi leo risus, porta ac consectetur ac, vestibulum at eros. Duis mollis, est non commodo luctus, nisi erat porttitor ligula, eget lacinia odio sem nec elit.</p>
<p class="quote-name">- Dana Whitlock -</p>
<p class="quote-role">Businessman</p>

<div class="news-panel"></div>
<div class="news-divider"></div>
<h2 class="news-title">Latest News</h2>
<a class="news-all">Read All News →</a>
<article class="news-item" style="top:1864px">
  <div class="news-thumb" role="img" aria-label="News thumbnail photo"></div>
  <h4>Sem Porta Mollis Parturient</h4>
  <div class="news-meta"><span>◷ 21 Mar 2014</span><span>▭ 0 Comment</span></div>
</article>
<article class="news-item" style="top:1950px">
  <div class="news-thumb" role="img" aria-label="News thumbnail photo"></div>
  <h4>Nullam Lorem Mattis Purus</h4>
  <div class="news-meta"><span>◷ 21 Mar 2014</span><span>▭ 0 Comment</span></div>
</article>
<article class="news-item" style="top:2038px;border-bottom:none">
  <div class="news-thumb" role="img" aria-label="News thumbnail photo"></div>
  <h4>Nibh Sem Sit Ullamcorper</h4>
  <div class="news-meta"><span>◷ 21 Mar 2014</span><span>▭ 0 Comment</span></div>
</article>

<div class="cta-blue"></div>
<svg class="cta-call" width="560" height="112" viewBox="0 0 560 112" aria-hidden="true">
  <polygon points="0,0 556,0 520,112 0,112" fill="#b4b4b4"/>
  <polygon points="548,0 556,0 520,112 512,112" fill="#8a8a8a"/>
</svg>
<p class="cta-small">You can call us toll free</p>
<p class="cta-phone">(888) 555-0162</p>
<h3 class="quote-title">Request a Free Quote</h3>
<div class="field" style="left:583px;width:193px">Name</div>
<div class="field" style="left:794px;width:192px">Email</div>
<a class="btn-subscribe">Subscribe</a>

<footer class="site-footer">
  <h3 class="footer-head" style="left:98px">Quick Links</h3>
  <ul class="footer-links" style="left:100px"><li>Home</li><li>How it works</li><li>Features</li><li>Pricing</li><li>Contact us</li></ul>
  <ul class="footer-links" style="left:252px"><li>Terms of use</li><li>Reseller</li><li>Sitemap</li><li>Uptime Report</li></ul>

  <h3 class="footer-head" style="left:415px">Contact Us</h3>
  <div class="contact-row" style="top:112px"><span class="contact-ico"></span><div style="font-size:11px;line-height:15px"><b>HARBORLINE</b><br>418 West Alder Avenue<br>Lakeside, FL. 32899</div></div>
  <div class="contact-row" style="top:168px;align-items:center"><span class="contact-ico"></span>555-010-2244</div>
  <div class="contact-row" style="top:213px;align-items:center"><span class="contact-ico"></span>info@harborline.example</div>

  <h3 class="footer-head" style="left:689px">Follow Us</h3>
  <div class="social-row" style="top:113px"><span class="social-ico" style="background:#2f6fb5"></span>NEWSFEED</div>
  <div class="social-row" style="top:153px"><span class="social-ico" style="background:#2fa8df"></span>UPDATES</div>
  <div class="social-row" style="top:200px"><span class="social-ico" style="background:#e35b2c"></span>CIRCLES</div>

  <div class="brand"><span class="brand-dot"></span>Brisklane IT</div>
</footer>
<div class="copyright">Brisklane IT All rights reserved. Copyright 2016-2017</div>

</body>
</html>
```